KVB Business Card Design

We need a business card that emphasizes consulting services worldwide. The name of the company is KVB Consulting Group. We provide consulting services across several industries including but not limited to commodities, telecom, manufacturing, logistics, marketing and operations. We would like to see a creative design that emphasizes the global aspect, including Latin America and US markets, as well the bilingual nature of the service offerings.

The contact information section should include icons to represent the following data:
1) Name, Title and Company Name
2) Mobile Number
3) Talkline ID
4) Email
5) Web Page
6) Location

We would like to see a card that emphasizes the worldwide concept. The back of the card should be simple, including only the logo (or a portion of the logo) and the slogan.

We would also like to see business cards in a booklet format. The colors to be used should be the same combination of colors used in the logos attached to this brief.

The logo design and some business card examples from Artvane Hub are attached for reference on style and look.

Target Market(s)

International business executives, 45-65 years of age, bilingual

Industry/Entity Type

Marketing

Colors
0792cd
34a7d8
85cae6
ffffff
cee9f5
ecf7fb

Requirements
Must have
• Please follow colors in logo attached.

2) Mobile Number
3) Talkline ID
4) Email
5) Web Page
6) Location
Nice to have
• Global concept, consulting profile, diverse industry focus
Should not have
• No black color

```html
<!DOCTYPE html>
<html lang="en">
<head>
<meta charset="utf-8">
<title>KVB Consulting Group – Business Card</title>
<link rel="stylesheet" href="https://fonts.googleapis.com/css2?family=Arimo:wght@700&family=Oswald:wght@600&family=Roboto+Condensed:ital,wght@1,700&family=Tinos:ital@1&display=swap">
<style>
  :root {
    --paper: #ffffff;
    --brand-deep: #0792cd;
    --brand-mid: #34a7d8;
    --brand-light: #85cae6;
    --brand-pale: #cee9f5;
    --brand-mist: #ecf7fb;
  }
  * { margin: 0; padding: 0; box-sizing: border-box; }
  html, body { width: 1200px; height: 704px; overflow: hidden; background: var(--paper); }
  .card { position: relative; width: 1200px; height: 704px; background: var(--paper); }
  .frame-outer {
    position: absolute; left: 22px; top: 22px; width: 1155px; height: 660px;
    border: 3px solid var(--brand-deep);
  }
  .frame-inner {
    position: absolute; left: 44px; top: 46px; width: 1109px; height: 613px;
    border: 3px solid var(--brand-light);
    overflow: hidden;
  }
  .world-backdrop {
    position: absolute; inset: 0;
    background:
      radial-gradient(circle at 190px 340px, var(--brand-pale) 0, var(--brand-mist) 190px, rgba(255,255,255,0) 260px),
      radial-gradient(ellipse 440px 270px at 820px 210px, var(--brand-mist) 0, rgba(255,255,255,0) 100%);
  }
  .person-title {
    position: absolute; left: 100px; top: 58px;
    display: flex; align-items: center; gap: 14px;
    font-family: "Oswald", sans-serif; font-weight: 600; font-size: 54px;
    color: var(--brand-mid); line-height: 1;
  }
  .person-title svg { width: 38px; height: 38px; flex: none; }
  .accent-bar { position: absolute; left: 806px; width: 199px; height: 11px; }
  .accent-bar--deep { top: 99px; background: var(--brand-deep); }
  .accent-bar--light { top: 194px; background: var(--brand-light); }
  .company-box {
    position: absolute; left: 196px; top: 163px; width: 566px; height: 63px;
    border: 3px solid var(--brand-mid); background: var(--paper);
    display: flex; align-items: center; justify-content: center;
    font-family: "Arimo", sans-serif; font-weight: 700; font-size: 40px;
    color: var(--brand-deep); letter-spacing: 1.5px;
  }
  .services {
    position: absolute; left: 293px; top: 246px;
    font-family: "Tinos", serif; font-style: italic; font-size: 34px;
    line-height: 50px; letter-spacing: 2px; color: var(--brand-deep);
  }
  .contact {
    position: absolute; left: 150px; top: 470px; width: 900px;
    display: grid; grid-template-columns: 470px 430px; row-gap: 10px;
    font-family: "Roboto Condensed", sans-serif; font-style: italic; font-weight: 700;
    font-size: 24px; line-height: 36px; color: var(--brand-deep);
  }
  .contact-line { display: flex; align-items: center; gap: 12px; white-space: nowrap; }
  .contact-icon { width: 30px; height: 30px; flex: none; }
</style>
</head>
<body>
  <div class="card">
    <div class="frame-outer"></div>
    <div class="frame-inner">
      <div class="world-backdrop" role="img" aria-label="Soft light-blue globe with network lines and world map showing the Americas"></div>
    </div>

    <div class="person-title">
      <svg viewBox="0 0 24 24" aria-hidden="true"><circle cx="12" cy="12" r="12" fill="#34a7d8"/><circle cx="12" cy="9" r="4" fill="#fff"/><path d="M5 19c1.5-4 12.5-4 14 0" fill="#fff"/></svg>
      <span>Lena Ortiz, President &amp; CEO</span>
    </div>
    <div class="accent-bar accent-bar--deep"></div>

    <div class="company-box">KVB Consulting Group</div>
    <div class="accent-bar accent-bar--light"></div>

    <p class="services">
      Consulting services across several<br>
      industries (not limited to commodities)<br>
      industries, telecom, manufacturing<br>
      logistics, marketing and operations.
    </p>

    <div class="contact">
      <div class="contact-line">
        <svg class="contact-icon" viewBox="0 0 24 24" aria-hidden="true"><circle cx="12" cy="12" r="12" fill="#34a7d8"/><rect x="6" y="8" width="12" height="9" rx="1" fill="#fff"/><path d="M6.5 8.5l5.5 4.5 5.5-4.5" fill="none" stroke="#34a7d8" stroke-width="1.4"/></svg>
        <span>Email: kvbcg@nubemail.com</span>
      </div>
      <div class="contact-line">
        <svg class="contact-icon" viewBox="0 0 24 24" aria-hidden="true"><circle cx="12" cy="12" r="12" fill="#34a7d8"/><circle cx="12" cy="12" r="6.5" fill="none" stroke="#fff" stroke-width="1.4"/><ellipse cx="12" cy="12" rx="2.8" ry="6.5" fill="none" stroke="#fff" stroke-width="1.2"/><path d="M5.5 12h13" stroke="#fff" stroke-width="1.2"/></svg>
        <span>Web: www.kvbcgroup.net</span>
      </div>
      <div class="contact-line">
        <svg class="contact-icon" viewBox="0 0 24 24" aria-hidden="true"><circle cx="12" cy="12" r="12" fill="#34a7d8"/><path d="M6 7h12v8h-7l-3.5 3v-3H6z" fill="#fff"/></svg>
        <span>Talkline ID: kvbconsultinggroup</span>
      </div>
      <div class="contact-line">
        <svg class="contact-icon" viewBox="0 0 24 24" aria-hidden="true"><circle cx="12" cy="12" r="12" fill="#34a7d8"/><path d="M12 19s-5-5.2-5-8.5a5 5 0 0 1 10 0C17 13.8 12 19 12 19z" fill="#fff"/><circle cx="12" cy="10.5" r="1.8" fill="#34a7d8"/></svg>
        <span>Location: Bay Vista, FL</span>
      </div>
      <div class="contact-line">
        <svg class="contact-icon" viewBox="0 0 24 24" aria-hidden="true"><circle cx="12" cy="12" r="12" fill="#34a7d8"/><rect x="8.5" y="5.5" width="7" height="13" rx="1.5" fill="#fff"/><circle cx="12" cy="16.3" r="0.9" fill="#34a7d8"/></svg>
        <span>Mobile: +1 305 555-0147</span>
      </div>
    </div>
  </div>
</body>
</html>
```